Brightpath Holdings Business Card

Create a two sided, high gloss, quality business card for Brightpath Holdings.

Target Market(s)

People wanting to purchase, scale, and sell businesses.

Industry/Entity Type

Entrepreneurs

Contact Information for Business Card

One line: Dana Corwell, CPA, CMA Another line: Entrepreneur & Investor Another line: Business Ownership Transition Expert Another line: Multi-State Licensed Real Estate Broker Phone 954-BRTPATH (278-7284) Email Dana@Brightpath Holdings.com Website www.Brightpath.com

Requirements
Must have
• Black Card, logo on one side, all other information on the other side including a small logo.
Nice to have
• Possibly add a tagline "Helping entrepreneurs live a life they don't need a vacation from"
Should not have
• There will not be a mailing address on these cards.

```html
<!DOCTYPE html>
<html lang="en">
<head>
<meta charset="UTF-8">
<title>Brightpath Holdings Business Card</title>
<link href="https://fonts.googleapis.com/css2?family=Montserrat:wght@400;500;700&display=swap" rel="stylesheet">
<style>
  :root {
    --backdrop: #2b2b2c;
    --card: #121212;
    --gold: #c9a445;
    --gold-light: #e6cf7f;
    --text: #cfcfcf;
  }
  * { margin: 0; padding: 0; box-sizing: border-box; }
  html, body { width: 1200px; height: 1039px; overflow: hidden; }
  body {
    background: var(--backdrop);
    font-family: "Montserrat", sans-serif;
    display: flex;
    flex-direction: column;
    align-items: center;
    justify-content: center;
    gap: 48px;
  }
  .card {
    position: relative;
    width: 800px;
    height: 457px;
    background: var(--card);
    box-shadow: 0 18px 40px rgba(0,0,0,.45);
  }
  /* Front */
  .front .brand {
    position: absolute;
    left: 0; right: 0; top: 150px;
    display: flex; align-items: center; justify-content: center; gap: 22px;
  }
  .brand-dot {
    width: 58px; height: 58px; border-radius: 50%;
    background: var(--gold);
  }
  .brand-name {
    color: var(--gold);
    font-weight: 700;
    font-size: 54px;
    letter-spacing: .5px;
  }
  .tagline {
    position: absolute;
    left: 0; right: 0; bottom: 70px;
    text-align: center;
    color: var(--text);
    font-size: 19px;
    letter-spacing: 1.2px;
  }
  /* Back */
  .back .brand {
    position: absolute; right: 60px; top: 52px;
    display: flex; align-items: center; gap: 10px;
  }
  .back .brand-dot { width: 26px; height: 26px; }
  .back .brand-name { font-size: 24px; }
  .rule {
    position: absolute; left: 60px; right: 60px; top: 130px;
    height: 2px;
    background: linear-gradient(90deg, var(--gold-light), var(--gold));
  }
  .person { position: absolute; left: 60px; top: 190px; }
  .person-name {
    color: var(--gold); font-weight: 700; font-size: 30px; margin-bottom: 10px;
  }
  .person-role { color: var(--text); font-size: 17px; line-height: 1.5; }
  .contacts {
    position: absolute; left: 60px; bottom: 52px;
    list-style: none; color: var(--text); font-size: 17px; line-height: 1.8;
  }
  .web {
    position: absolute; right: 60px; top: 150px;
    list-style: none; color: var(--text); font-size: 16px; line-height: 1.8;
  }
  .contacts li, .web li { display: flex; align-items: center; gap: 10px; }
  .icon { width: 15px; height: 15px; flex: none; }
</style>
</head>
<body>

<section class="card front">
  <div class="brand">
    <span class="brand-dot"></span>
    <span class="brand-name">Brightpath Holdings</span>
  </div>
  <p class="tagline">Helping entrepreneurs live a life they don't need a vacation from</p>
</section>

<section class="card back">
  <div class="brand">
    <span class="brand-dot"></span>
    <span class="brand-name">Brightpath Holdings</span>
  </div>
  <div class="rule"></div>

  <ul class="web">
    <li>
      <svg class="icon" viewBox="0 0 16 16"><circle cx="8" cy="8" r="7" fill="none" stroke="#c9a445" stroke-width="1.5"/><ellipse cx="8" cy="8" rx="3" ry="7" fill="none" stroke="#c9a445" stroke-width="1.2"/><line x1="1" y1="8" x2="15" y2="8" stroke="#c9a445" stroke-width="1.2"/></svg>
      www.BrightpathHoldings.com
    </li>
    <li>
      <svg class="icon" viewBox="0 0 16 16"><circle cx="8" cy="8" r="7" fill="none" stroke="#c9a445" stroke-width="1.5"/><ellipse cx="8" cy="8" rx="3" ry="7" fill="none" stroke="#c9a445" stroke-width="1.2"/><line x1="1" y1="8" x2="15" y2="8" stroke="#c9a445" stroke-width="1.2"/></svg>
      www.Brightpath.com
    </li>
  </ul>

  <div class="person">
    <h1 class="person-name">Dana Corwell, CPA, CMA</h1>
    <p class="person-role">Entrepreneur &amp; Investor</p>
    <p class="person-role">Business Ownership Transition Expert</p>
    <p class="person-role">Multi-State Licensed Real Estate Broker</p>
  </div>

  <ul class="contacts">
    <li>
      <svg class="icon" viewBox="0 0 16 16"><path d="M3 1.5l3 .5 1 3.5-2 1.2a8 8 0 0 0 4.3 4.3l1.2-2 3.5 1 .5 3c-1 1-2 1.3-3 1A13 13 0 0 1 1.5 4.5c-.3-1 0-2 1.5-3z" fill="#c9a445"/></svg>
      954-BRTPATH (278-7284)
    </li>
    <li>
      <svg class="icon" viewBox="0 0 16 16"><rect x="1" y="3" width="14" height="10" fill="#c9a445"/><path d="M1 3l7 6 7-6" fill="none" stroke="#121212" stroke-width="1.3"/></svg>
      Dana@Brightpath Holdings.com
    </li>
  </ul>
</section>

</body>
</html>
```